Tooth Fairy Certificates with a Brown Tooth Fairy character on it (animation)
Tooth Certificate
I needs a name and date slot
also boxes for checks or stars next to each word
- clean
- shiny
- needs more brushing

Great Job, I'm so Proud of you! keep up the great brushing!

I need 4 per 11x8 page or 2- 5' 7 per page.

```html
<!DOCTYPE html>
<html lang="en">
<head>
<meta charset="utf-8">
<title>Tooth Fairy Certificate</title>
<link rel="stylesheet" href="https://fonts.googleapis.com/css2?family=Kaushan+Script&family=Itim&family=Alfa+Slab+One&family=Chewy&display=swap">
<style>
  :root {
    --paper: #faf6f0;
    --frame: #8a3a22;
    --title: #7c1a2c;
    --label: #c47a38;
    --rule: #f0c9a4;
    --check-text: #a07062;
    --box: #2a2a2a;
    --cheer: #cf8436;
    --gold-light: #f0c070;
    --gold-dark: #c98a3c;
    --tooth: #ffffff;
    --tooth-edge: #e6ded4;
    --fairy-light: #d98a5a;
    --fairy-dark: #7a3a22;
  }
  * { margin: 0; padding: 0; box-sizing: border-box; }
  html, body { width: 858px; height: 1200px; overflow: hidden; background: var(--paper); }
  .certificate { position: relative; width: 858px; height: 1200px; background: var(--paper); overflow: hidden; }
  .frame { position: absolute; left: 72px; top: 86px; width: 696px; height: 1027px; border: 3px solid var(--frame); }
  .decor { position: absolute; inset: 0; width: 858px; height: 1200px; }
  .title {
    position: absolute; left: 0; width: 858px; text-align: center;
    font-family: "Kaushan Script", cursive; color: var(--title); font-size: 74px; line-height: 1;
  }
  .title-line-1 { top: 178px; }
  .title-line-2 { top: 286px; }
  .field-label {
    position: absolute; left: 0; width: 858px; text-align: center;
    font-family: "Itim", sans-serif; color: var(--label); font-size: 29px; line-height: 1;
  }
  .field-label.recipient { top: 434px; }
  .field-label.date { top: 573px; }
  .field-rule { position: absolute; left: 159px; width: 541px; height: 1.5px; background: var(--rule); }
  .field-rule.recipient { top: 512px; }
  .field-rule.date { top: 652px; }
  .check-box { position: absolute; width: 50px; height: 50px; border: 1.5px solid var(--box); background: transparent; }
  .check-label {
    position: absolute; font-family: "Alfa Slab One", serif; color: var(--check-text);
    font-size: 31px; line-height: 50px; letter-spacing: 0.5px;
  }
  .cheer {
    position: absolute; left: 180px; top: 942px; width: 540px; text-align: center;
    font-family: "Chewy", cursive; color: var(--cheer); font-size: 45px; line-height: 50px;
  }
  .fairy-art {
    position: absolute; left: 0; top: 790px; width: 250px; height: 410px;
    background: linear-gradient(160deg, var(--fairy-light), var(--fairy-dark));
    border-radius: 50% 50% 30% 40% / 30% 30% 20% 20%;
    opacity: 0.9;
  }
</style>
</head>
<body>
<main class="certificate">
  <div class="frame"></div>

  <svg class="decor" viewBox="0 0 858 1200" aria-hidden="true">
    <defs>
      <linearGradient id="gold" x1="0" y1="0" x2="1" y2="1">
        <stop offset="0" stop-color="var(--gold-light)"/>
        <stop offset="1" stop-color="var(--gold-dark)"/>
      </linearGradient>
      <symbol id="star" viewBox="-1 -1 2 2">
        <polygon points="0,-1 0.235,-0.324 0.951,-0.309 0.380,0.124 0.588,0.809 0,0.4 -0.588,0.809 -0.380,0.124 -0.951,-0.309 -0.235,-0.324" fill="url(#gold)"/>
      </symbol>
    </defs>
    <use href="#star" x="6" y="84" width="60" height="60"/>
    <use href="#star" x="530" y="64" width="50" height="50"/>
    <use href="#star" x="238" y="120" width="30" height="30"/>
    <use href="#star" x="108" y="245" width="146" height="146"/>
    <use href="#star" x="396" y="243" width="50" height="50"/>
    <use href="#star" x="318" y="460" width="32" height="32"/>
    <use href="#star" x="76" y="458" width="18" height="18"/>
    <use href="#star" x="562" y="707" width="30" height="30"/>
    <use href="#star" x="786" y="724" width="16" height="16"/>
    <use href="#star" x="648" y="796" width="128" height="128"/>
    <use href="#star" x="476" y="876" width="50" height="50"/>
    <use href="#star" x="264" y="890" width="16" height="16"/>
    <use href="#star" x="804" y="1004" width="54" height="54"/>
    <use href="#star" x="364" y="1030" width="34" height="34"/>
    <use href="#star" x="718" y="1147" width="18" height="18"/>
    <polygon points="76,780 88,814 124,816 96,838 106,872 76,852 46,872 56,838 28,816 64,814" fill="none" stroke="var(--gold-dark)" stroke-width="2"/>
  </svg>

  <div role="img" aria-label="Tooth illustration" style="position:absolute;left:62px;top:90px;width:112px;height:122px;background:var(--tooth);border:2px solid var(--tooth-edge);border-radius:40% 40% 30% 30%;"></div>
  <div role="img" aria-label="Tooth illustration with sparkle rays" style="position:absolute;left:640px;top:126px;width:150px;height:172px;background:radial-gradient(circle,var(--tooth) 55%,#f3e3d6 100%);border:2px solid var(--tooth-edge);border-radius:40% 40% 30% 30%;"></div>
  <div role="img" aria-label="Small tooth illustration" style="position:absolute;left:34px;top:525px;width:72px;height:84px;background:var(--tooth);border:2px solid var(--tooth-edge);border-radius:40% 40% 30% 30%;"></div>
  <div role="img" aria-label="Small tooth illustration" style="position:absolute;left:748px;top:502px;width:72px;height:82px;background:var(--tooth);border:2px solid var(--tooth-edge);border-radius:40% 40% 30% 30%;"></div>

  <h1 class="title title-line-1">Tooth Fairy</h1>
  <h1 class="title title-line-2">Certificate</h1>

  <p class="field-label recipient">This Certificate is Proudly to:</p>
  <div class="field-rule recipient"></div>
  <p class="field-label date">Lost the tooth on the:</p>
  <div class="field-rule date"></div>

  <div class="check-box" style="left:184px;top:747px;"></div>
  <span class="check-label" style="left:253px;top:747px;">NEEDS MORE BRUSHING</span>
  <div class="check-box" style="left:217px;top:822px;"></div>
  <span class="check-label" style="left:298px;top:822px;">SHINY</span>
  <div class="check-box" style="left:454px;top:822px;"></div>
  <span class="check-label" style="left:520px;top:822px;">CLEAN</span>

  <div class="fairy-art" role="img" aria-label="Brown-haired tooth fairy character in an orange dress with brown wings, flying"></div>

  <p class="cheer">Great Job, I'm so Proud of you! Keep up the great brushing!</p>
</main>
</body>
</html>
```